TRUCK WASH OUTDOOR DRIVE THROUGH MENU CONTEST

WE NEED A DRIVE THROUGH MENU WITH OUR SERVICES AND PRICES. I HAVE ATTACHED A FEW EXAMPLES THAT I STARTED.

I WANT THIS TO BE EYE CATCHING WITH BRIGHT COLORS

Target Market(s)

TRUCK WASH AND DETAIL SHOP, TRANSPORTATION.

Requirements
Must have
• INCORPORATE MY LOGO INTO THE SIGN.
• FINAL PROJECT MUST BE IN .AI FORMAT.
• COMPANY COLORS ARE RED AND BLUE

```html
<!DOCTYPE html>
<html lang="en">
<head>
<meta charset="utf-8">
<title>Highway Hauler Wash – Drive Through Menu</title>
<link rel="stylesheet" href="https://fonts.googleapis.com/css2?family=Black+Ops+One&family=Audiowide&display=swap">
<style>
  :root{
    --red-deep:#8e0b0b;
    --red:#d8150f;
    --red-bright:#ff2a1a;
    --star-red:#e3141b;
    --white:#ffffff;
    --black:#0b0b0b;
    --tab-dark:#3a0606;
    --tab-mid:#5e1210;
    --panel-a:rgba(120,70,170,0.78);
    --panel-b:rgba(70,110,230,0.85);
    --panel-c:rgba(120,160,255,0.9);
    --curl:#2a0a2e;
    --logo-blue:#2b7bff;
  }
  *{margin:0;padding:0;box-sizing:border-box}
  html,body{width:848px;height:1200px;overflow:hidden;background:var(--red-deep)}
  .menu-board{
    position:relative;width:848px;height:1200px;overflow:hidden;
    background:
      radial-gradient(ellipse at 60% 35%, var(--red-bright) 0%, var(--red) 40%, var(--red-deep) 100%);
  }
  .hero-trucks{
    position:absolute;left:211px;top:94px;width:503px;height:158px;
    background:linear-gradient(90deg, rgba(120,0,0,.0), rgba(110,0,0,.45) 20%, rgba(110,0,0,.45) 80%, rgba(120,0,0,0));
    border-radius:8px;
  }
  .brand{
    position:absolute;left:0;top:28px;width:100%;text-align:center;
  }
  .brand-mark{
    width:84px;height:84px;border-radius:50%;background:var(--star-red);
    border:4px solid var(--white);margin:0 auto 14px;
  }
  .brand-name{
    font-family:"Black Ops One",sans-serif;font-size:40px;color:var(--white);
    letter-spacing:1px;line-height:1;
  }
  .price-star{position:absolute;left:77px;width:280px;height:280px}
  .price-star svg{position:absolute;inset:0;overflow:visible}
  .price-label{
    position:absolute;inset:0;display:flex;flex-direction:column;align-items:center;justify-content:center;
    font-family:"Black Ops One",sans-serif;color:var(--white);line-height:.95;
    text-shadow:3px 3px 0 var(--black);padding-top:10px;
  }
  .price-label .currency{font-size:44px}
  .price-label .amount{font-size:54px}
  .package{position:absolute;left:416px;width:432px}
  .package-tab{
    position:relative;margin-left:34px;width:212px;height:46px;
    background:linear-gradient(90deg,var(--tab-dark),var(--tab-mid) 70%,rgba(94,18,16,.6));
    font-family:"Black Ops One",sans-serif;font-size:34px;color:var(--white);
    padding-left:14px;line-height:48px;letter-spacing:1px;
  }
  .package-tab::before{
    content:"";position:absolute;left:-14px;top:0;border-style:solid;
    border-width:23px 14px 23px 0;border-color:transparent var(--tab-dark) transparent transparent;
  }
  .package-panel{
    position:relative;
    background:linear-gradient(90deg,var(--panel-a),var(--panel-b) 55%,var(--panel-c));
    border-radius:14px 0 0 14px;
    padding:14px 10px 16px 58px;
    font-family:"Audiowide",sans-serif;font-size:19px;color:var(--white);
    line-height:20px;letter-spacing:1.5px;text-transform:uppercase;
  }
  .package-panel::before,.package-panel::after{
    content:"";position:absolute;left:10px;right:0;border-top:2px dashed rgba(255,255,255,.85);
  }
  .package-panel::before{top:6px}
  .package-panel::after{bottom:6px}
  .package-curl{
    width:36px;height:26px;margin-top:-4px;
    background:var(--curl);border-radius:0 0 0 20px;
  }
  .service-list{list-style:none}
</style>
</head>
<body>
<main class="menu-board">
  <div class="hero-trucks" role="img" aria-label="Faint illustration of semi trucks behind the brand name"></div>

  <header class="brand">
    <div class="brand-mark"></div>
    <div class="brand-name">Highway Hauler Wash</div>
  </header>

  <div class="price-star" style="top:211px">
    <svg viewBox="-140 -140 280 280" aria-hidden="true">
      <polygon transform="translate(10,8)" fill="var(--black)" points="0,-135 32.3,-44.5 128.4,-41.7 52.3,17 79.4,109.2 0,55 -79.4,109.2 -52.3,17 -128.4,-41.7 -32.3,-44.5"/>
      <polygon fill="var(--star-red)" stroke="var(--white)" stroke-width="7" stroke-linejoin="miter" points="0,-135 32.3,-44.5 128.4,-41.7 52.3,17 79.4,109.2 0,55 -79.4,109.2 -52.3,17 -128.4,-41.7 -32.3,-44.5"/>
    </svg>
    <div class="price-label"><span class="currency">$</span><span class="amount">130</span></div>
  </div>
  <div class="price-star" style="top:446px">
    <svg viewBox="-140 -140 280 280" aria-hidden="true">
      <polygon transform="translate(10,8)" fill="var(--black)" points="0,-135 32.3,-44.5 128.4,-41.7 52.3,17 79.4,109.2 0,55 -79.4,109.2 -52.3,17 -128.4,-41.7 -32.3,-44.5"/>
      <polygon fill="var(--star-red)" stroke="var(--white)" stroke-width="7" points="0,-135 32.3,-44.5 128.4,-41.7 52.3,17 79.4,109.2 0,55 -79.4,109.2 -52.3,17 -128.4,-41.7 -32.3,-44.5"/>
    </svg>
    <div class="price-label"><span class="currency">$</span><span class="amount">120</span></div>
  </div>
  <div class="price-star" style="top:668px">
    <svg viewBox="-140 -140 280 280" aria-hidden="true">
      <polygon transform="translate(10,8)" fill="var(--black)" points="0,-135 32.3,-44.5 128.4,-41.7 52.3,17 79.4,109.2 0,55 -79.4,109.2 -52.3,17 -128.4,-41.7 -32.3,-44.5"/>
      <polygon fill="var(--star-red)" stroke="var(--white)" stroke-width="7" points="0,-135 32.3,-44.5 128.4,-41.7 52.3,17 79.4,109.2 0,55 -79.4,109.2 -52.3,17 -128.4,-41.7 -32.3,-44.5"/>
    </svg>
    <div class="price-label"><span class="currency">$</span><span class="amount">100</span></div>
  </div>
  <div class="price-star" style="top:891px">
    <svg viewBox="-140 -140 280 280" aria-hidden="true">
      <polygon transform="translate(10,8)" fill="var(--black)" points="0,-135 32.3,-44.5 128.4,-41.7 52.3,17 79.4,109.2 0,55 -79.4,109.2 -52.3,17 -128.4,-41.7 -32.3,-44.5"/>
      <polygon fill="var(--star-red)" stroke="var(--white)" stroke-width="7" points="0,-135 32.3,-44.5 128.4,-41.7 52.3,17 79.4,109.2 0,55 -79.4,109.2 -52.3,17 -128.4,-41.7 -32.3,-44.5"/>
    </svg>
    <div class="price-label"><span class="currency">$</span><span class="amount">80</span></div>
  </div>

  <section class="package" style="top:278px">
    <h2 class="package-tab">PLATINUM</h2>
    <div class="package-panel">
      <ul class="service-list">
        <li>Pre-soak</li><li>Soap and scrub</li><li>Rinse</li><li>Tireshine</li><li>Platinum protection</li>
      </ul>
    </div>
    <div class="package-curl"></div>
  </section>

  <section class="package" style="top:493px">
    <h2 class="package-tab">GOLD</h2>
    <div class="package-panel">
      <ul class="service-list">
        <li>Pre-soak</li><li>Soap and scrub</li><li>Rinse</li><li>Tireshine</li><li>Wet X polish</li>
      </ul>
    </div>
    <div class="package-curl"></div>
  </section>

  <section class="package" style="top:720px">
    <h2 class="package-tab">SILVER</h2>
    <div class="package-panel">
      <ul class="service-list">
        <li>Pre-soak</li><li>Soap and scrub</li><li>Rinse</li><li>Tireshine</li>
      </ul>
    </div>
    <div class="package-curl"></div>
  </section>

  <section class="package" style="top:941px">
    <h2 class="package-tab">EXPRESS</h2>
    <div class="package-panel" style="padding-top:28px;padding-bottom:30px">
      <ul class="service-list">
        <li>Pre-soak</li><li>Soap and scrub</li><li>Rinse</li>
      </ul>
    </div>
    <div class="package-curl"></div>
  </section>
</main>
</body>
</html>
```